Christmas Banner for frontpage of website

New online scarf store just opened needs a Christmas Banner stating Free Delivery (UK only). Also if it could incorporate guaranteed Christmas delivery if ordered before 18th (might be too wordy though?) I would really like it to bring some colour to the page. The page is currently black and white with a pink accent and is very simple which is why I would like something modern and elegant, simple but with some colour. It is a shopify store I understand the banner size should be 950px by 290px the website is www.velmorrow.co.uk

Target Market(s)

Ladies

Industry/Entity Type

Store

Requirements
Should not have
• Not to look tacky.

```html
<!DOCTYPE html>
<html lang="en">
<head>
<meta charset="utf-8">
<title>Free Delivery – Christmas Banner</title>
<link rel="stylesheet" href="https://fonts.googleapis.com/css2?family=Lobster+Two:ital,wght@1,700&family=Open+Sans:wght@800&display=swap">
<style>
  :root {
    --pink-light: #f6b3ef;
    --pink-mid: #ec8ee4;
    --pink-deep: #df6ad4;
    --band: #dc55d1;
    --headline: #fcd3f7;
    --headline-shadow: #b0359f;
    --white: #ffffff;
    --floor-top: #ffffff;
    --floor-bottom: #d9d9d9;
    --note: #b5b5b5;
    --tree-dark: #5f6d69;
    --tree-mid: #8d9894;
    --tree-glow: #c77dc0;
  }
  html, body {
    margin: 0;
    padding: 0;
    overflow: hidden;
    background: var(--white);
  }
  .banner {
    position: relative;
    width: 1200px;
    height: 366px;
    overflow: hidden;
    background: var(--pink-mid);
    font-family: "Open Sans", Arial, sans-serif;
  }
  .banner__frost {
    position: absolute;
    inset: 0;
    background:
      radial-gradient(ellipse 260px 160px at 560px 60px, rgba(255,255,255,0.22), transparent 70%),
      radial-gradient(ellipse 300px 180px at 980px 110px, rgba(255,255,255,0.18), transparent 70%),
      radial-gradient(ellipse 240px 150px at 420px 250px, rgba(255,255,255,0.16), transparent 70%),
      radial-gradient(ellipse 280px 140px at 880px 300px, rgba(255,255,255,0.14), transparent 70%),
      radial-gradient(ellipse at 55% 40%, var(--pink-light) 0%, var(--pink-mid) 55%, var(--pink-deep) 100%);
  }
  .banner__floor {
    position: absolute;
    left: 0;
    right: 0;
    bottom: 0;
    height: 36px;
    background: linear-gradient(to bottom, var(--floor-top), var(--floor-bottom));
  }
  .banner__tree {
    position: absolute;
    left: 19px;
    top: 6px;
    width: 260px;
    height: 354px;
    border-radius: 50% 50% 22px 22px / 30% 30% 22px 22px;
    background:
      radial-gradient(ellipse at 50% 55%, var(--tree-mid) 0%, var(--tree-dark) 75%),
      var(--tree-dark);
    box-shadow: inset 0 0 40px rgba(199,125,192,0.45);
  }
  .banner__art {
    position: absolute;
    inset: 0;
  }
  .band { fill: var(--band); }
  .headline {
    font-family: "Lobster Two", "Brush Script MT", cursive;
    font-style: italic;
    font-weight: 700;
    fill: var(--headline);
  }
  .headline--shadow { fill: var(--headline-shadow); opacity: 0.5; }
  .tagline {
    font-family: "Open Sans", Arial, sans-serif;
    font-weight: 800;
    fill: var(--white);
  }
  .banner__note {
    position: absolute;
    right: 14px;
    bottom: 6px;
    margin: 0;
    font-size: 15px;
    font-weight: 800;
    color: var(--note);
  }
</style>
</head>
<body>
<div class="banner">
  <div class="banner__frost" role="img" aria-label="Frosted pink background with faint snowflake pattern"></div>
  <div class="banner__floor"></div>
  <div class="banner__tree" role="img" aria-label="Frosted Christmas tree decorated with pink lights"></div>

  <svg class="banner__art" width="1200" height="366" viewBox="0 0 1200 366" xmlns="http://www.w3.org/2000/svg">
    <polygon class="band" points="250,259 1200,183 1200,227 250,299"/>
    <text class="tagline" x="285" y="290" font-size="30" textLength="858" lengthAdjust="spacingAndGlyphs"
          transform="rotate(-4.2 285 290)">Guaranteed Christmas delivery if ordered before 18th!</text>

    <text class="headline headline--shadow" x="294" y="214" font-size="150" textLength="790" lengthAdjust="spacingAndGlyphs"
          transform="rotate(-6 294 214)">Free Delivery</text>
    <text class="headline" x="290" y="209" font-size="150" textLength="790" lengthAdjust="spacingAndGlyphs"
          transform="rotate(-6 290 209)">Free Delivery</text>
    <text class="headline" x="1100" y="64" font-size="34">*</text>
  </svg>

  <p class="banner__note">* UK Only</p>
</div>
</body>
</html>
```